Poster design for "A Frame" Sign

I need a design for an A Frame sign. Measurements and Specifications here:
http://www.trimpaneldepot.com.au/pg/a-boards/XQRTMNDLW-Print-Specs.pdf

Actually, it will need to be two designs, one with an arrow pointing left and one with an arrow pointing right, otherwise exactly the same.

LOGO to be used is attached. Colours of design should match logo and should also include orange tones.

The A Frame sign is to be put on the driveway of my home studio at a main road in a residential suburban area. Cars drive by at around 50 km/h, so there needs to be an eye catcher that there is a nurturing home massage studio here.

Logo can be left or right, somehow incorporated into the text below:
-
[Big header, ideally "LeHavre" font]
Marindi Healing
Massage Studio

[slightly smaller font, serif, with bullet points]
- Relaxation Massage
- Remedial Massage
- Pregnancy Massage
- Kahuna Massage

[big Arrow to the left/right - one for each side of the frame]

[sans serif font, same size as above]
Bookings essential!
ph 0491 786 514
www.marindihealing.com.au

[serif font, same as above]
EFTPOS and instant health fund claims available.
-

Industry/Entity Type

Residential

Colors
f37022

```html
<!DOCTYPE html>
<html lang="en">
<head>
<meta charset="utf-8">
<title>Marindi Healing – A Frame Sign</title>
<link rel="stylesheet" href="https://fonts.googleapis.com/css2?family=Arimo:ital,wght@0,700;1,700&family=Patrick+Hand+SC&display=swap">
<style>
  :root {
    --backdrop: #141414;
    --sign-orange: #f35d2a;
    --white: #ffffff;
    --logo-plum: #7a1a4a;
    --logo-pink: #e8509a;
  }
  html, body {
    margin: 0;
    padding: 0;
    width: 1200px;
    height: 900px;
    overflow: hidden;
    background: var(--backdrop);
  }
  .canvas {
    position: relative;
    width: 1200px;
    height: 900px;
    background: var(--backdrop);
  }
  .sign {
    position: absolute;
    left: 347px;
    top: 97px;
    width: 498px;
    height: 735px;
    background: var(--sign-orange);
    color: var(--white);
    font-family: "Arimo", Arial, sans-serif;
    font-weight: 700;
  }
  .sign-frame {
    position: absolute;
    left: 16px;
    top: 18px;
    width: 453px;
    height: 689px;
    border: 6px solid var(--white);
  }
  .brand-mark {
    position: absolute;
    left: 188px;
    top: 39px;
    width: 122px;
    height: 122px;
    border-radius: 50%;
    background: var(--logo-plum);
    display: flex;
    align-items: center;
    justify-content: center;
  }
  .brand-mark-name {
    font-family: "Patrick Hand SC", cursive;
    font-size: 26px;
    color: var(--white);
  }
  .centered {
    position: absolute;
    left: 0;
    width: 498px;
    text-align: center;
    white-space: nowrap;
  }
  .title {
    font-family: "Patrick Hand SC", cursive;
    font-weight: 400;
    line-height: 1;
  }
  .title-name { top: 172px; font-size: 58px; }
  .title-studio { top: 225px; font-size: 42px; }
  .services {
    position: absolute;
    left: 111px;
    top: 289px;
    margin: 0;
    padding: 0;
    list-style: none;
    font-style: italic;
    font-size: 25px;
  }
  .services li {
    height: 38.4px;
    line-height: 38.4px;
  }
  .services li::before {
    content: "";
    display: inline-block;
    width: 12px;
    height: 12px;
    margin-right: 6px;
    border-radius: 50%;
    background: var(--white);
    vertical-align: 2px;
  }
  .direction-arrow {
    position: absolute;
    left: 0;
    top: 0;
  }
  .bookings { top: 518px; font-size: 25px; }
  .phone { top: 547px; font-size: 66px; letter-spacing: -1px; transform: scaleX(0.9); }
  .web-band {
    position: absolute;
    left: 23px;
    top: 615px;
    width: 452px;
    height: 35px;
    background: var(--white);
    color: var(--sign-orange);
    font-size: 25px;
    line-height: 35px;
    text-align: center;
  }
  .payments {
    top: 657px;
    font-size: 25px;
    line-height: 28.5px;
  }
</style>
</head>
<body>
<main class="canvas">
  <section class="sign" aria-label="Marindi Healing Massage Studio A frame sign">
    <div class="sign-frame"></div>

    <div class="brand-mark"><span class="brand-mark-name">Marindi</span></div>

    <h1 class="centered title title-name" style="margin:0">Marindi Healing</h1>
    <h2 class="centered title title-studio" style="margin:0">Massage Studio</h2>

    <ul class="services">
      <li>Relaxation Massage</li>
      <li>Remedial Massage</li>
      <li>Pregnancy Massage</li>
      <li>Kahuna Massage</li>
    </ul>

    <svg class="direction-arrow" width="498" height="735" viewBox="0 0 498 735" aria-label="Arrow pointing right">
      <polygon fill="#ffffff" points="73,455 397,455 397,443 438,481 397,520 397,508 73,508 107,481"/>
    </svg>

    <p class="centered bookings" style="margin:0">Bookings Essential!</p>
    <p class="centered phone" style="margin:0">0491 786 514</p>
    <div class="web-band">www.marindihealing.com.au</div>
    <p class="centered payments" style="margin:0">EFTPOS and instant health<br>fund claims available</p>
  </section>
</main>
</body>
</html>
```